New Website for QWRB Holdings (Property Leasing Company in New Haven)

Design a fully functioning website for a real estate property leasing company. The company has a few properties in New Haven, CT and would like to provide an option for its tenants to pay their rent online. The company should have the ability to generate unique account log in username and password for its tenants so they can make online payments through ACH the website. (The ACH processing part will be coordinated with the bank).

Please take a look at all the pictures I uploaded of New Haven especially the area around Marlow College, you will find that the general style is Gothic and charming.

Also please make use of the pictures of the two properties I have attached to the description.

Please keep Holdings page, Contact Us Page , About Us Page, and please add a page entitled "Tenants".

On the Holdings page I would like to see on the left hand side an interactive map of new haven (Please see a map attached), split by New Haven's neighbourhoods, and showing my properties as pins of sort on the map (I can send you the addresses of the properties upon request). On the same page on the right side I want to see a drop down menu that includes list of New Haven Neighbourhoods. When a neighbourhood is selected you can see in the space underneath the drop-down menu the properties we have in that neighbourhood in large thumbnail format. Also on the map you can see the pins corresponding to those properties change colour. A user can either click on the pin or on the thumbnails to have view more pictures of the property and some details in text.

The tenants page should prompt a login to access- I like your idea of having the company name in two colours, one for QWRB and another for Holdings.Please let me know if you have any questions along the way

-------------------------------------------------------------------------------
Property Descriptions for Holdings Page
The Larch Lodge,

Neighbourhood: Westville
Name: Silas Brennaway House
Building Style: Queen Anne Style
Address: 418 Pellwin Road, New Haven, CT 06515
Number of Units: 3
Unit Names: Unit 1, Unit 2, Unit 3

Property Description

This Westiville home was built in 1897, historically known as The Silas Brennaway House, it is an example of the Queen Anne style. The large carriage house is still intact and sits in the lovely, expansive back garden! An outstanding architectural feature of the house is the turret, giving the home prominence on Pellwin Road. This well maintained home has renovated kitchens in all units, the first floor has granite and red oak cabinetry. New baths and central air in all apartments. All newer mechanicals for each unit, all natural gas. The entire house has replacement windows. The new back deck overlooks the back garden and carriage house. The front steps and porch have also been rebuilt. Roof has 30 year architectural singles and approximately 15 years old, the chimney has just been lined.

Unit 1 Description:

2 Bedrooms, 6 rooms in total.
Amenities: Dishwasher, Central Air, Gas Heating, Porch

Unit 2 Description:

2 Bedrooms, 5 rooms in total.
Amenities: Dishwasher, Central Air, Gas Heating, Balcony

Unit 3 Description:

2 Bedrooms, 4 rooms in total.
Amenities: Dishwasher, Central Air, Gas Heating

The Fern Lodge:

Neighbourhood: East Rock
Name: 64 Birchmere
Building Style: Victorian
Address: 64 Birchmere Lane, New Haven, CT 06511
Number of Units: 2
Unit Names: Unit 1, and Unit 2

Property Description

East Rock incredibly charming newly renovated 2 family on quiet tree-lined block. Tenants are responsible for all utilities (gas heat, electricity and cable). Small pets are possible with landlord approval. Tenants has use of shared yard, laundry in the basement and on street parking only. Located steps away from gourmet markets & minutes to Downtown New Haven, Marlow & local hospitals. Fascinating backyard. This is a feel good house!

Unit 1 Description:

Area:
1100 soft, 3 Bedrooms, 5 rooms in total.
Amenities: In unit Washer and Dryer, Central Air, Gas Heating, Porch, Backyard

Unit 2 Description:

Area: 2,820 sqft
5 Bedrooms, 8 rooms in total.
Amenities: In unit Washer and Dryer, Dishwasher, Central Air, and Gas Heating

Target Market(s)

1-3 bedroom Renting Market around Marlow College and New Haven Community

Industry/Entity Type

Real Estate

Coding

Coded - Design and coding required

Number of Pages Required

4 page

Font styles to use
Other font styles liked:
• Helvetica

Colors
85cae6
cee9f5
d9d9d9
9d9d9d

Requirements
Must have
• Payment page with login (accounts can only be created by administrator)
• A page showcasing the properties (Professional photos to be uploaded shortly)
• A page for technical support, contact information and so forth
• Home page
Nice to have
• A professional, but stylish design. Not too colourful, something with pastel colours
Should not have
• A lot of colours, any pop-ups,

```html
<!DOCTYPE html>
<html lang="en">
<head>
<meta charset="utf-8">
<title>QWRB Holdings</title>
<link rel="stylesheet" href="https://fonts.googleapis.com/css2?family=Arimo:ital,wght@0,400;0,700;1,700&family=Open+Sans:ital,wght@0,300;0,400;0,700;1,300&display=swap">
<style>
  :root {
    --ink: #000000;
    --white: #ffffff;
    --green: #4f9d10;
    --green-bright: #5cb81e;
    --grey-text: #8c8c8c;
    --grey-light: #a9a9a9;
    --rule: #d9d9d9;
  }
  * { box-sizing: border-box; margin: 0; padding: 0; }
  html, body { width: 1200px; height: 2216px; overflow: hidden; background: var(--white); }
  body { position: relative; font-family: "Open Sans", Arial, sans-serif; }

  .site-header {
    position: absolute; left: 0; top: 0; width: 1200px; height: 100px;
    background: var(--ink); display: flex; align-items: center; justify-content: space-between;
    padding: 0 40px 0 72px;
  }
  .brand { font-family: "Arimo", Arial, sans-serif; font-weight: 700; font-size: 62px; color: var(--green-bright); letter-spacing: 1px; }
  .main-nav { display: flex; gap: 56px; }
  .main-nav a { font-family: "Arimo", Arial, sans-serif; font-weight: 700; font-size: 23px; color: var(--white); text-decoration: none; letter-spacing: 0.5px; }

  .hero {
    position: absolute; left: 0; top: 100px; width: 1200px; height: 760px;
    background: linear-gradient(180deg, #c7d7e6 0%, #9fb2c4 22%, #7d7f7a 40%, #8b6a4e 62%, #6a5a48 80%, #4f4a40 100%);
  }
  .hero-title {
    position: absolute; left: 0; top: 218px; width: 1200px; text-align: center;
    font-family: "Arimo", Arial, sans-serif; font-weight: 700; font-size: 90px; line-height: 1;
    color: var(--white); white-space: nowrap;
  }
  .search {
    position: absolute; left: 208px; top: 452px; width: 784px; height: 72px; display: flex;
  }
  .search-field {
    flex: 1; background: var(--white); display: flex; align-items: center; gap: 18px; padding-left: 46px;
    font-size: 22px; color: var(--grey-light);
  }
  .search-button {
    width: 152px; background: var(--green); color: var(--white); font-size: 26px;
    display: flex; align-items: center; justify-content: center;
  }

  .listing-band {
    position: absolute; left: 0; width: 1200px; height: 82px; background: var(--green);
    padding-left: 34px; display: flex; align-items: center; white-space: nowrap;
    font-family: "Arimo", Arial, sans-serif; font-weight: 700; font-style: italic; font-size: 62px; color: var(--white);
  }
  .listing-photo { position: absolute; left: 40px; width: 548px; height: 428px; }
  .listing-info { position: absolute; left: 696px; width: 490px; }
  .listing-kicker { font-weight: 300; font-style: italic; font-size: 80px; color: var(--grey-light); line-height: 1; white-space: nowrap; }
  .listing-address { font-weight: 700; font-size: 48px; color: var(--green); margin-top: 8px; line-height: 1.1; white-space: nowrap; }
  .listing-text { font-size: 37px; color: var(--grey-text); line-height: 52px; margin-top: 28px; }
  .listing-location { display: flex; gap: 26px; align-items: flex-start; margin-top: 18px; }
  .listing-location p { font-size: 21px; color: var(--grey-text); line-height: 1.3; }

  .site-footer {
    position: absolute; left: 0; top: 1988px; width: 1200px; height: 228px; background: var(--ink);
  }
  .footer-nav { position: absolute; top: 40px; left: 0; width: 1200px; display: flex; justify-content: center; gap: 64px; }
  .footer-nav a { font-size: 20px; color: var(--green); text-decoration: none; letter-spacing: 0.5px; }
  .social { position: absolute; top: 104px; left: 432px; width: 336px; height: 72px; display: flex; justify-content: space-between; }
  .social span { width: 72px; height: 72px; border-radius: 50%; background: var(--green); display: block; }
</style>
</head>
<body>
  <header class="site-header">
    <div class="brand">QWRB</div>
    <nav class="main-nav">
      <a href="#">HOLDINGS</a>
      <a href="#">TENANTS</a>
      <a href="#">ABOUT US</a>
      <a href="#">CONTACT US</a>
    </nav>
  </header>

  <section class="hero" role="img" aria-label="Aerial view of New Haven rooftops and autumn trees with the harbour and sky beyond">
    <h1 class="hero-title">MAIN TITLE GOES HERE</h1>
    <div class="search">
      <div class="search-field">
        <svg width="34" height="34" viewBox="0 0 34 34" aria-hidden="true">
          <circle cx="14" cy="14" r="10" fill="none" stroke="#9d9d9d" stroke-width="3.5"/>
          <line x1="21.5" y1="21.5" x2="31" y2="31" stroke="#9d9d9d" stroke-width="4" stroke-linecap="round"/>
        </svg>
        <span>Type postcode or address</span>
      </div>
      <div class="search-button">Search</div>
    </div>
  </section>

  <h2 class="listing-band" style="top:888px">UNDERTITLE ONE GOES HERE</h2>
  <div class="listing-photo" style="top:980px; background:linear-gradient(180deg,#8fb3d6 0%,#6e8a5a 35%,#4f6e3c 70%,#3c5530 100%)" role="img" aria-label="Photo of a Queen Anne style house with a front porch and lawn"></div>
  <div class="listing-info" style="top:996px">
    <p class="listing-kicker">FOR LEASE</p>
    <p class="listing-address">Address goes here</p>
    <p class="listing-text">Ex ius viderer fierent, est assum omnes facilisis ex, eruditi quaerendum his te.</p>
    <div class="listing-location">
      <svg width="44" height="58" viewBox="0 0 44 58" aria-hidden="true">
        <path d="M22 3C11.5 3 4 10.8 4 21c0 13 18 33 18 33s18-20 18-33C40 10.8 32.5 3 22 3z" fill="none" stroke="#4f9d10" stroke-width="4"/>
        <circle cx="22" cy="21" r="6.5" fill="none" stroke="#4f9d10" stroke-width="4"/>
      </svg>
      <p>42 Harlow Road<br>ELMCOTE<br>EC14 2RT</p>
    </div>
  </div>

  <h2 class="listing-band" style="top:1446px">UNDERTITLE TWO GOES HERE</h2>
  <div class="listing-photo" style="top:1536px; background:linear-gradient(180deg,#6f7d5e 0%,#8d9290 35%,#6c6f70 65%,#5a5250 100%)" role="img" aria-label="Photo of a Victorian two-family house with an exterior staircase"></div>
  <div class="listing-info" style="top:1554px">
    <p class="listing-kicker">FOR LEASE</p>
    <p class="listing-address">Address goes here</p>
    <p class="listing-text">Ex ius viderer fierent, est assum omnes facilisis ex, eruditi quaerendum his te.</p>
    <div class="listing-location">
      <svg width="44" height="58" viewBox="0 0 44 58" aria-hidden="true">
        <path d="M22 3C11.5 3 4 10.8 4 21c0 13 18 33 18 33s18-20 18-33C40 10.8 32.5 3 22 3z" fill="none" stroke="#4f9d10" stroke-width="4"/>
        <circle cx="22" cy="21" r="6.5" fill="none" stroke="#4f9d10" stroke-width="4"/>
      </svg>
      <p>42 Harlow Road<br>ELMCOTE<br>EC14 2RT</p>
    </div>
  </div>

  <footer class="site-footer">
    <nav class="footer-nav">
      <a href="#">HOLDINGS</a>
      <a href="#">TENANTS</a>
      <a href="#">ABOUT US</a>
      <a href="#">CONTACT US</a>
    </nav>
    <div class="social" aria-label="Social links">
      <span></span><span></span><span></span><span></span>
    </div>
  </footer>
</body>
</html>
```